KBS PSYCHIATRIC ASSOCIATES INC NEEDS A LOGO AND BUSINESS CARD

I am changing my business name and need a fresh logo and business card. I run a psychiatric consultation service and also provide both in-person and telehealth psychiatric care.

Janet R Farrow DNP, MSN, APRN, PMHNP-BC, CRNP, FAANP
8315 27th AVE CT NW
Cedar Bay, OR 97412
318-555-0172

```html
<!DOCTYPE html>
<html lang="en">
<head>
<meta charset="utf-8">
<title>KBS Psychiatric Associates – Business Card</title>
<link rel="stylesheet" href="https://fonts.googleapis.com/css2?family=Montserrat:wght@400;500;700&display=swap">
<style>
  :root {
    --bg: #26272b;
    --brand-blue: #1273be;
    --brand-green: #3bb54a;
    --ink: #222222;
    --paper: #ffffff;
    --rule: #2b2b2b;
  }
  * { box-sizing: border-box; margin: 0; padding: 0; }
  html, body {
    width: 1200px; height: 799px; overflow: hidden;
    background: var(--bg);
    font-family: "Montserrat", sans-serif;
  }
  .stage {
    position: relative; width: 1200px; height: 799px;
    display: flex; align-items: center; justify-content: center; gap: 50px;
  }
  .card {
    position: relative; width: 520px; height: 297px;
    border-radius: 18px; overflow: hidden;
    box-shadow: 0 14px 30px rgba(0,0,0,.45);
  }

  /* Front */
  .card--front { background: var(--brand-blue); display: flex; align-items: center; justify-content: center; }
  .brand { display: flex; align-items: center; gap: 16px; }
  .brand__dot { width: 74px; height: 74px; border-radius: 50%; flex: none; }
  .brand__name { font-weight: 700; line-height: 1.05; letter-spacing: .04em; }
  .brand__name .big { display: block; font-size: 54px; letter-spacing: .02em; }
  .brand__name .small { display: block; font-size: 19px; }
  .card--front .brand__dot { background: var(--paper); }
  .card--front .brand__name { color: var(--paper); }

  /* Back */
  .card--back { background: var(--paper); }
  .bands { position: absolute; inset: 0; }
  .card--back .brand { position: absolute; top: 30px; right: 44px; gap: 12px; }
  .card--back .brand__dot { width: 56px; height: 56px; background: var(--brand-green); }
  .card--back .brand__name { color: var(--brand-blue); }
  .card--back .brand__name .big { font-size: 40px; }
  .card--back .brand__name .small { font-size: 14px; }

  .person { position: absolute; left: 36px; top: 138px; }
  .person__name { color: var(--brand-blue); font-weight: 700; font-size: 27px; }
  .person__creds { color: var(--ink); font-size: 13.5px; margin-top: 4px; }
  .divider { position: absolute; left: 36px; right: 36px; top: 204px; height: 1px; background: var(--rule); }

  .contact { position: absolute; left: 36px; top: 214px; font-size: 14px; color: var(--ink); }
  .contact__row { display: flex; align-items: center; gap: 10px; height: 24px; }
  .contact__row svg { width: 15px; height: 15px; fill: var(--brand-green); flex: none; }
  .address { position: absolute; right: 36px; top: 214px; font-size: 13.5px; color: var(--ink); text-align: right; line-height: 24px; }
</style>
</head>
<body>
<main class="stage">

  <section class="card card--front" aria-label="Card front">
    <div class="brand">
      <span class="brand__dot"></span>
      <p class="brand__name"><span class="big">KBS</span><span class="small">PSYCHIATRIC</span><span class="small">ASSOCIATES</span></p>
    </div>
  </section>

  <section class="card card--back" aria-label="Card back">
    <svg class="bands" viewBox="0 0 520 297" preserveAspectRatio="none" aria-hidden="true">
      <polygon points="0,0 250,0 244,10 0,10" fill="var(--brand-green)"/>
      <polygon points="250,0 520,0 520,10 244,10" fill="var(--brand-blue)"/>
      <polygon points="0,287 300,287 294,297 0,297" fill="var(--brand-blue)"/>
      <polygon points="300,287 520,287 520,297 294,297" fill="var(--brand-green)"/>
    </svg>

    <div class="brand">
      <span class="brand__dot"></span>
      <p class="brand__name"><span class="big">KBS</span><span class="small">PSYCHIATRIC</span><span class="small">ASSOCIATES</span></p>
    </div>

    <div class="person">
      <h1 class="person__name">Janet R Farrow</h1>
      <p class="person__creds">DNP, MSN, APRN, PMHNP-BC, CRNP, FAANP</p>
    </div>

    <div class="divider"></div>

    <div class="contact">
      <p class="contact__row">
        <svg viewBox="0 0 24 24" aria-hidden="true"><path d="M6.6 10.8a15.1 15.1 0 0 0 6.6 6.6l2.2-2.2c.3-.3.7-.4 1-.2 1.1.4 2.3.6 3.6.6.6 0 1 .4 1 1V20c0 .6-.4 1-1 1A17 17 0 0 1 3 4c0-.6.4-1 1-1h3.5c.6 0 1 .4 1 1 0 1.3.2 2.5.6 3.6.1.3 0 .7-.2 1z"/></svg>
        318-555-0172
      </p>
      <p class="contact__row">
        <svg viewBox="0 0 24 24" aria-hidden="true"><path d="M2 5h20v14H2zM3.5 6.5 12 13l8.5-6.5z" fill-rule="evenodd"/></svg>
        jrfarrow@farrowmail.com
      </p>
    </div>

    <p class="address">8315 27th AVE CT NW<br>Cedar Bay, OR 97412</p>
  </section>

</main>
</body>
</html>
```